Promotion flyer for chair massage

What i need is a design for a 2 page flyer. Im gonna give it to a company so their employe can learn about the service and how they can take an appointements with us. The text is in french because i work in a french company.
On first page(FRONT PAGE) i want the name of the company VELORAMAX inc.
and bellow : Massothérapie sur chaise en entreprise
On the second page(INSIDE) i want the benefits :
Les Bienfaits
- DIMINUTION DU STRESS
- AMÉLIORATION DU BIEN-ÊTRE PHYSIQUE ET PSYCHOLOGIQUE
- AUGMENTATION DE L’ÉNERGIE
- SOULAGE LES MAUX DE DOS ET DE TÊTE
- AMÉLIORE VOTRE QUALITÉ DE SOMMEIL
On the third page (INSIDE) I want the steps to take an appointment :
Obtenez votre massage en quelques clics
1. Allez sur https://www.bookalyte.example/veloramax
2. Choisir le nombre de minute désirer (10-15-20-30)
3. Choisir votre thérapeute
4. Choisir votre emplacement (lieu de travail)
5. Choisir votre plage horaire
6. Remplir votre fiche (Prénom-Nom-Email-#téléphone)
7. Aussi simple que ça !! À bientôt !
On the final page i want the text so they can contact me :
CONTACTEZ-NOUS
Mail : Info@veloramax.example
Tél. 514-276-9032
Site web : Veloramax.example
If you can respect the same kind of design that i already did in the past i would love it :)
Bank employee
Massage Therapy

```html
<!DOCTYPE html>
<html lang="fr">
<head>
<meta charset="utf-8">
<title>VELORAMAX inc. – Massothérapie sur chaise en entreprise</title>
<link rel="stylesheet" href="https://fonts.googleapis.com/css2?family=Bebas+Neue&family=Oswald:wght@500&family=Lato:wght@400&display=swap">
<style>
  :root{
    --bg:#bcbdbf;
    --page:#f5f6f7;
    --ink:#121a24;
    --blue:#1f78c1;
    --blue-deep:#155fa3;
    --blue-light:#4aa8e0;
    --white:#ffffff;
    --text:#1b222b;
  }
  *{margin:0;padding:0;box-sizing:border-box}
  html,body{width:899px;height:1200px;overflow:hidden;background:var(--bg)}
  .canvas{position:relative;width:899px;height:1200px}
  .artwork{position:absolute;inset:0}
  .heading,.brand,.cover-title{font-family:"Bebas Neue",sans-serif;letter-spacing:.3px}
  .abs{position:absolute;white-space:nowrap}

  .brand{color:var(--white);font-size:31px;line-height:1;display:flex;align-items:center;gap:7px}
  .brand-dot{width:15px;height:15px;border-radius:50%;background:var(--white)}
  .brand--small{color:var(--blue-deep);font-size:22px}
  .brand--small .brand-dot{background:var(--blue-deep);width:11px;height:11px}
  .brand-tagline{font-family:"Lato",sans-serif;font-size:5px;letter-spacing:1px;color:#5b6570}

  .contact{font-family:"Lato",sans-serif;font-size:10px;color:var(--white);display:flex;align-items:center;gap:8px}
  .contact svg{width:10px;height:10px;stroke:var(--blue-light);fill:none;stroke-width:1.4}

  .company{font-family:"Lato",sans-serif;font-size:11.5px;color:var(--blue-light)}
  .cover-title{color:var(--white);font-size:23px;line-height:1}

  .heading{color:var(--ink);font-size:19px;line-height:1}
  .heading-rule{height:1.5px;width:73px;background:var(--blue)}

  .benefit{position:absolute;width:150px;margin-left:-75px;text-align:center}
  .benefit svg{width:46px;height:46px;stroke:var(--blue-light);fill:none;stroke-width:1.6;stroke-linecap:round;stroke-linejoin:round;display:block;margin:0 auto 4px}
  .benefit-label{font-family:"Oswald",sans-serif;font-weight:500;font-size:7.6px;color:var(--ink);letter-spacing:.1px}

  .steps{position:absolute;left:484px;top:731px;list-style:none}
  .step{display:flex;align-items:center;gap:11px;height:35.6px;font-family:"Lato",sans-serif;font-size:11.5px;color:var(--text)}
  .step-num{width:15px;height:15px;border:1px solid var(--blue-light);color:var(--blue-light);font-size:9.5px;display:flex;align-items:center;justify-content:center}
</style>
</head>
<body>
<div class="canvas">
  <svg class="artwork" width="899" height="1200" viewBox="0 0 899 1200" aria-hidden="false">
    <defs>
      <linearGradient id="photoBlue" x1="0" y1="0" x2="1" y2="1">
        <stop offset="0" stop-color="#2b86d2"/>
        <stop offset="1" stop-color="#10509a"/>
      </linearGradient>
      <linearGradient id="skinTone" x1="0" y1="0" x2="1" y2="1">
        <stop offset="0" stop-color="#d9cfc6"/>
        <stop offset="1" stop-color="#8a6f5c"/>
      </linearGradient>
    </defs>

    <!-- Spread 1: back cover + front cover -->
    <rect class="page" x="72" y="70" width="762" height="494" fill="var(--page)"/>
    <polygon points="144,284 452,206 452,392" fill="var(--blue)"/>
    <polygon points="250,258 452,206 452,300" fill="var(--blue-deep)" opacity=".55"/>
    <polygon points="72,260 452,392 452,564 72,564" fill="var(--ink)"/>
    <polygon points="452,206 834,112 834,472 452,392" fill="url(#photoBlue)" role="img" aria-label="Photo d'un massothérapeute massant les épaules d'un employé assis"/>
    <polygon points="452,392 834,472 834,564 452,564" fill="var(--ink)"/>
    <line x1="452" y1="70" x2="452" y2="564" stroke="#000" stroke-opacity=".08"/>

    <!-- Spread 2: inside pages -->
    <rect class="page" x="72" y="644" width="762" height="494" fill="var(--page)"/>
    <polygon points="72,950 452,1020 452,1138 72,1138" fill="url(#photoBlue)" role="img" aria-label="Photo d'une massothérapeute traitant une personne sur une chaise de massage"/>
    <polygon points="452,1020 834,1096 834,1138 452,1138" fill="var(--ink)"/>
    <circle cx="378" cy="1012" r="54" fill="var(--white)"/>
    <circle cx="378" cy="1012" r="51" fill="url(#skinTone)" role="img" aria-label="Gros plan de mains massant la nuque"/>
    <line x1="452" y1="644" x2="452" y2="1138" stroke="#000" stroke-opacity=".08"/>
  </svg>

  <!-- Back cover -->
  <div class="abs brand" style="left:90px;top:401px">VELORAMAX<span class="brand-dot"></span></div>
  <div class="abs contact" style="left:96px;top:464px">
    <svg viewBox="0 0 10 10"><path d="M2 1l2 2-1 1.3a6 6 0 0 0 2.7 2.7L7 6l2 2-1.3 1.3C4.5 9 1 5.5.7 2.3z"/></svg>514-276-9032</div>
  <div class="abs contact" style="left:96px;top:493px">
    <svg viewBox="0 0 10 10"><path d="M1 4l4-3 4 3v5H1zM1 4l4 3 4-3"/></svg>Info@veloramax.example</div>
  <div class="abs contact" style="left:96px;top:526px">
    <svg viewBox="0 0 10 10"><circle cx="5" cy="5" r="4"/><path d="M1 5h8M5 1c-2 2.5-2 5.5 0 8M5 1c2 2.5 2 5.5 0 8"/></svg>Veloramax.example</div>

  <!-- Front cover -->
  <div class="abs brand brand--small" style="left:472px;top:102px">VELORAMAX<span class="brand-dot"></span></div>
  <div class="abs brand-tagline" style="left:503px;top:126px">MASSOTHÉRAPIE EN ENTREPRISE</div>
  <div class="abs company" style="left:470px;top:493px">VELORAMAX inc.</div>
  <div class="abs cover-title" style="left:470px;top:516px">MASSOTHÉRAPIE SUR CHAISE EN ENTREPRISE</div>

  <!-- Benefits page -->
  <h2 class="abs heading" style="left:90px;top:678px">LES BIENFAITS</h2>
  <div class="abs heading-rule" style="left:90px;top:708px"></div>

  <div class="benefit" style="left:173px;top:718px">
    <svg viewBox="0 0 46 46"><path d="M6 30h8l8 4h8l8-6M6 26v12h5V26z"/><path d="M23 28c0-8 0-12-7-16 0 6 2 10 7 12M23 22c2-7 7-10 12-10 0 7-5 10-12 10"/></svg>
    <div class="benefit-label">DIMINUTION DU STRESS</div>
  </div>
  <div class="benefit" style="left:317px;top:718px">
    <svg viewBox="0 0 46 46"><path d="M23 6c-5 8-8 12-8 16a8 8 0 0 0 16 0c0-4-3-8-8-16z"/><path d="M20 24a3 3 0 0 0 3 3M6 34c10 6 24 6 34 0M10 39c8 3 18 3 26 0"/></svg>
    <div class="benefit-label">AUGMENTATION DU BIEN-ÊTRE</div>
  </div>
  <div class="benefit" style="left:173px;top:798px">
    <svg viewBox="0 0 46 46"><circle cx="23" cy="22" r="9"/><path d="M19 31v6h8v-6M20 41h6M23 5v4M9 22H5M41 22h-4M12 11l3 3M34 11l-3 3"/></svg>
    <div class="benefit-label">AUGMENTATION DE L’ÉNERGIE</div>
  </div>
  <div class="benefit" style="left:317px;top:798px">
    <svg viewBox="0 0 46 46"><circle cx="17" cy="15" r="6"/><path d="M5 40v-8c0-5 5-8 12-8s12 3 12 8v8z"/><circle cx="32" cy="18" r="5"/><path d="M31 26c6 0 10 2 10 7v7h-12"/></svg>
    <div class="benefit-label">HAUSSE DU SENTIMENT D’APPARTENANCE</div>
  </div>
  <div class="benefit" style="left:173px;top:878px">
    <svg viewBox="0 0 46 46"><circle cx="26" cy="18" r="13"/><path d="M26 10v9h6M4 32v8h5v-8zM9 34h10l6 3h8"/></svg>
    <div class="benefit-label">DIMINUTION DE L’ABSENTÉISME</div>
  </div>
  <div class="benefit" style="left:317px;top:878px">
    <svg viewBox="0 0 46 46"><path d="M10 24c0-8 7-12 15-12 9 0 15 5 15 12 0 4-2 7-5 9v5h-5v-3h-8v3h-5v-5c-2-1-4-3-4-5H7v-6h3z"/><path d="M20 12l-2-5 6 4M33 22h.1"/></svg>
    <div class="benefit-label">AUGMENTATION DE LA PRODUCTIVITÉ</div>
  </div>

  <!-- Booking steps page -->
  <h2 class="abs heading" style="left:484px;top:678px">OBTENEZ VOTRE MASSAGE EN QUELQUES CLICS</h2>
  <div class="abs heading-rule" style="left:483px;top:708px"></div>
  <ol class="steps">
    <li class="step"><span class="step-num">1</span>llez sur https://www.bookalyte.example/veloramax</li>
    <li class="step"><span class="step-num">2</span>Choisir le nombre de minute désirer (10-15-20-30)</li>
    <li class="step"><span class="step-num">3</span>Choisir votre thérapeute</li>
    <li class="step"><span class="step-num">4</span>Choisir votre emplacement (lieu de travail)</li>
    <li class="step"><span class="step-num">5</span>Choisir votre plage horaire</li>
    <li class="step"><span class="step-num">6</span>Remplir votre fiche (Prénom-Nom-Email-#téléphone)</li>
    <li class="step"><span class="step-num">7</span>Aussi simple que ça !! À bientôt !</li>
  </ol>
</div>
</body>
</html>
```